Website Design for my CNC machine Shop.

I need a new website for my Machining Company.

It can be a simple website that acts more like an "Online Business card" I has to highlight the services I provide and give Companies the confidence to engage my services.

I needs it to be a really modern or even a little futuristic promoting my Company.

I have just moved locations and have renovated the premises and would be great to let everyone know along with a new website.

If you can help with linking it to search engines to help get more exposure that would be great.

It needs to accommodate the three main services I provide which will include capacities of each machine (within that service) and maybe a couple images.
CNC Machining (5-axis, 3-axis)
EDM Wire cutting
3D Metal Printing
Along with home page and Contact page

I have two websites and you can use the txt from either/combination of these.
www.korvaltooling.com.au
(no longer do Laser Marking and etching but now do 3D metal Printing)
www.tarnquill.com.au

Happy to chat further with the designer

Company logo's provided.

For Images: I am happy to use Glimmerbay and can purchase any images you like
EDM Wire cut
https://www.glimmerbay-pics.com/search/edm-wire-cutting

CNC Machining:
https://www.glimmerbay-pics.com/search/vertical-cnc-machining
Don't use any with engines or motor vehicle parts

3D metal Printing
https://www.glimmerbay-pics.com/search/slm-metal-printing

Target Market(s)

Defence, Aerospace, Medical, HIgh Precision

Industry/Entity Type

Mechanical Engineering

Coding

Coded - Design and coding required

Number of Pages Required

5+ page

Requirements
Must have
• Home page, 3 services, Contacts. Can add image to each of the services

```html
<!DOCTYPE html>
<html lang="en">
<head>
<meta charset="utf-8">
<title>Korval Precision Machinists</title>
<link href="https://fonts.googleapis.com/css2?family=Inter:wght@400;500;600;700&family=Roboto:wght@400;500;700;900&display=swap" rel="stylesheet">
<style>
:root{
  --green:#3bb582;
  --navy:#0c1d2c;
  --navy-2:#13293b;
  --ink:#111417;
  --text:#3b3f44;
  --muted:#6b7075;
  --white:#ffffff;
  --line:#e3e6e8;
}
*{margin:0;padding:0;box-sizing:border-box}
html,body{width:1200px;height:4890px;overflow:hidden}
body{position:relative;font-family:"Inter",sans-serif;color:var(--text);background:var(--white)}
.abs{position:absolute}
h1,h2,h3{font-family:"Roboto",sans-serif;font-weight:500;color:var(--ink)}
.accent{color:var(--green)}
.btn{position:absolute;display:flex;align-items:center;justify-content:center;font-family:"Roboto",sans-serif;font-weight:500;font-size:15px;background:var(--green);color:var(--white)}
.photo{position:absolute}

/* hero */
.hero{left:0;top:0;width:1200px;height:650px;background:radial-gradient(circle at 72% 42%,#c8942e 0,#6a4a20 12%,#2a2a2c 30%,#121418 60%,#0b0c0f 100%)}
.logo{position:absolute;font-family:"Roboto",sans-serif}
.logo .name{display:block;font-weight:900;color:#e8e8e8;letter-spacing:2px}
.logo .tag{display:block;color:var(--green);font-family:"Inter",sans-serif;letter-spacing:2.5px}
.nav{position:absolute;top:30px;left:510px;display:flex;gap:0}
.nav a{color:var(--white);font-family:"Roboto",sans-serif;font-weight:500;font-size:13px;text-decoration:none;position:absolute;white-space:nowrap}
.hero .welcome{left:110px;top:285px;color:var(--white);font-family:"Roboto",sans-serif;font-weight:900;font-size:24px;letter-spacing:1px}
.hero .big{left:106px;top:325px;color:var(--white);font-family:"Roboto",sans-serif;font-weight:900;font-size:82px;letter-spacing:3px;line-height:1}
.hero .sub{left:110px;top:425px;color:var(--green);font-family:"Roboto",sans-serif;font-weight:700;font-size:29px;letter-spacing:1.5px}

/* about */
.frame{left:112px;top:737px;width:445px;height:433px;border:2px solid var(--ink)}
.frame::before{content:"";position:absolute;inset:6px;border:2px solid var(--ink)}
.frame::after{content:"";position:absolute;inset:12px;border:2px solid var(--ink)}
.about-text{left:642px;top:725px;width:455px}
.about-text h2{font-size:44px;margin-bottom:16px}
.about-text .lead{font-size:17px;font-weight:500;color:var(--ink);line-height:26px;margin-bottom:14px}
.about-text p{font-size:13px;line-height:26px;margin-bottom:12px}

/* factors */
.factors{left:0;top:1258px;width:1200px;height:370px;background:linear-gradient(90deg,#0b1a28,#15304a 50%,#0b1a28)}
.factors h2{position:absolute;left:110px;top:70px;color:var(--white);font-size:42px}
.factors p{position:absolute;left:112px;top:142px;width:470px;color:#d5dbe0;font-size:13px;line-height:30px}
.stat{position:absolute;width:190px;height:128px;background:var(--white);border:2px solid var(--ink);outline:3px solid var(--white);outline-offset:3px;text-align:center}
.stat svg{position:absolute;left:28px;top:30px}
.stat .num{position:absolute;left:90px;top:32px;color:var(--green);font-family:"Roboto",sans-serif;font-size:30px}
.stat .lbl{position:absolute;left:0;right:0;top:85px;font-family:"Roboto",sans-serif;font-size:14px;color:var(--ink)}

/* services */
.sec-title{position:absolute;left:0;width:1200px;text-align:center;font-size:42px}
.sec-intro{position:absolute;left:270px;width:660px;text-align:center;font-size:13px;line-height:26px}
.card{position:absolute;background:var(--white);box-shadow:0 0 10px rgba(0,0,0,.14)}
.svc{position:absolute;width:450px}
.svc h3{font-size:31px;margin-bottom:22px}
.svc p{font-size:13px;line-height:27px}
.svc ul{list-style:none;margin-top:18px}
.svc li{position:relative;padding-left:24px;font-size:12px;line-height:21px;margin-bottom:16px}
.svc li svg{position:absolute;left:0;top:4px}
.svc .key{color:var(--green);font-family:"Roboto",sans-serif;font-weight:500;font-size:15px;margin:6px 0 8px}
.svc .specs{display:grid;grid-template-columns:210px 210px;font-family:"Roboto",sans-serif;font-weight:500;font-size:14px;color:var(--ink);line-height:26px}

/* testimonials */
.testi{left:0;top:3318px;width:1200px;height:419px;background:linear-gradient(90deg,#0d2233,#16324a 50%,#0d2233)}
.testi h2{position:absolute;left:0;width:1200px;text-align:center;top:60px;color:var(--white);font-size:42px}
.quote{position:absolute;width:460px;color:#e4e9ee}
.avatar{position:absolute;width:78px;height:78px;border-radius:50%;background:linear-gradient(#8fb7d6,#3d6f95)}
.quote .who{position:absolute;left:100px;top:12px;font-family:"Roboto",sans-serif;font-weight:700;font-size:18px;color:var(--white)}
.quote .rate{position:absolute;left:100px;top:42px;display:flex;align-items:center;gap:4px}
.quote p{position:absolute;left:0;top:98px;width:460px;font-size:13px;line-height:29px;text-align:justify}
.arrow{position:absolute;width:22px;height:22px;border-radius:50%;background:var(--white)}

/* projects */
.proj-card{left:397px;top:3928px;width:405px;height:415px;background:var(--green);text-align:center;color:var(--white)}
.proj-card h3{color:var(--white);font-size:31px;margin-top:75px}
.proj-card p{width:320px;margin:22px auto 0;font-size:13px;font-weight:500;line-height:26px}
.proj-card a{display:inline-block;margin-top:22px;color:var(--white);font-size:13px;font-weight:600}

/* footer */
.footer{left:0;top:4420px;width:1200px;height:470px;background:var(--navy)}
.footer h4{font-family:"Roboto",sans-serif;font-weight:500;font-size:19px;color:var(--white);margin-bottom:24px}
.footer .col{position:absolute;top:190px}
.footer .col a,.footer .col span{display:block;color:#e2e7ec;font-size:13px;text-decoration:none;line-height:33px}
.vline{position:absolute;top:180px;width:1px;height:220px;background:#4a5b6a}
.row{display:flex;align-items:center;gap:22px;color:#e2e7ec;font-size:13px;height:52px}
.soc{display:flex;align-items:center;gap:20px;color:#e2e7ec;font-size:13px;height:40px}
.soc i{display:block;width:18px;height:18px;background:var(--white)}
.copy{position:absolute;left:0;width:1200px;text-align:center;top:445px;color:#d0d6dc;font-size:11px}
</style>
</head>
<body>

<!-- HERO -->
<section class="abs hero">
  <div class="photo" role="img" aria-label="Close-up of a CNC lathe cutting a brass part with sparks flying" style="inset:0"></div>
  <div class="logo" style="left:110px;top:18px">
    <span class="name" style="font-size:46px;line-height:1">KORVAL</span>
    <span class="tag" style="font-size:10px">PRECISION MACHINISTS</span>
  </div>
  <nav>
    <a class="nav-link" href="#" style="position:absolute;left:510px;top:30px;color:#fff;font:500 13px Roboto,sans-serif;text-decoration:none">Home</a>
    <a href="#" style="position:absolute;left:585px;top:30px;color:#fff;font:500 13px Roboto,sans-serif;text-decoration:none">About Us</a>
    <a href="#" style="position:absolute;left:685px;top:30px;color:#fff;font:500 13px Roboto,sans-serif;text-decoration:none">Services</a>
    <a href="#" style="position:absolute;left:778px;top:30px;color:#fff;font:500 13px Roboto,sans-serif;text-decoration:none">Projects</a>
    <a href="#" style="position:absolute;left:868px;top:30px;color:#fff;font:500 13px Roboto,sans-serif;text-decoration:none">Testimonials</a>
  </nav>
  <span class="btn" style="left:997px;top:22px;width:118px;height:38px">Contact Us</span>
  <div class="abs welcome">WELCOME TO</div>
  <div class="abs big">KORVAL</div>
  <div class="abs sub">PRECISION MACHINISTS</div>
  <span class="btn" style="left:110px;top:485px;width:124px;height:38px;background:#fff;color:var(--ink)">Get Started</span>
</section>

<!-- ABOUT -->
<div class="abs frame">
  <div class="photo" role="img" aria-label="Machinist operating a CNC control panel in the workshop" style="inset:20px;background:linear-gradient(135deg,#2b5f9e,#7fa9cf 55%,#8c7a66);z-index:1"></div>
</div>
<div class="abs about-text">
  <h2>About <span class="accent">Us</span></h2>
  <div class="lead">We are an innovative&nbsp; company that specialise in technical and creative engineering</div>
  <p>Our core sectors of expertise are in EDM wire cutting, 3D Metal Printing and CNC machining. With our combination of highly skilled staff and sophisticated machinery we offer a comprehensive and professional service.</p>
  <p>We are as diverse as our customer base, we are confident in providing an exceptionally high standard of quality in all facets of our company. Our factory is equipped with an extensive range of machinery allowing us to provide a full range of services such as wire and spark erosion, milling and turning.</p>
</div>
<span class="btn" style="left:642px;top:1123px;width:120px;height:38px">Read More</span>

<!-- FACTORS -->
<section class="abs factors">
  <h2>Some Important Factros</h2>
  <p>Lorem ipsum dolor sit amet, consectetur adipiscing elit, sed do eiusmod tempor incididunt ut labore et dolore magna aliqua. Ut enim ad minim veniam, quis nostrud exercitation ullamco laboris nisi ut aliquip ex ea commodo consequat. Duis aute irure dolor in reprehenderit in voluptate velit esse cillum dolore eu fugiat nulla pariatur.</p>
  <div class="stat" style="left:687px;top:60px">
    <svg width="40" height="36" viewBox="0 0 40 36" fill="none" stroke="#111" stroke-width="1.6"><rect x="6" y="4" width="20" height="14" rx="2"/><path d="M3 30l10-8 8 4 14-10"/></svg>
    <span class="num">34+</span><span class="lbl">Projects Completed</span></div>
  <div class="stat" style="left:895px;top:58px">
    <svg width="44" height="36" viewBox="0 0 44 36" fill="none" stroke="#111" stroke-width="1.6"><circle cx="14" cy="14" r="5"/><path d="M5 34c0-8 18-8 18 0"/><circle cx="30" cy="12" r="4"/><path d="M24 30c2-6 14-6 16 0"/></svg>
    <span class="num">10+</span><span class="lbl">Years Experince</span></div>
  <div class="stat" style="left:687px;top:198px">
    <svg width="44" height="38" viewBox="0 0 44 38" fill="none" stroke="#111" stroke-width="1.6"><circle cx="14" cy="10" r="6"/><path d="M3 36c0-10 22-10 22 0"/><circle cx="33" cy="22" r="7"/></svg>
    <span class="num">10+</span><span class="lbl">Experienced Workers</span></div>
  <div class="stat" style="left:895px;top:198px">
    <svg width="44" height="36" viewBox="0 0 44 36" fill="none" stroke="#111" stroke-width="1.6"><circle cx="22" cy="10" r="5"/><circle cx="9" cy="14" r="4"/><circle cx="35" cy="14" r="4"/><path d="M13 30c0-9 18-9 18 0M2 30c0-7 12-7 12-3M42 30c0-7-12-7-12-3"/></svg>
    <span class="num">347+</span><span class="lbl">Satisfied Customers</span></div>
</section>

<!-- SERVICES -->
<h2 class="sec-title" style="top:1702px">Our <span class="accent">Services</span></h2>
<p class="sec-intro" style="top:1780px">Being a high precision engineering company we offer a range of high qualtiy services to a veriaty of industries. With our work being so diverse we have listed a handful of many services we offer</p>

<div class="card" style="left:114px;top:1878px;width:978px;height:438px"></div>
<div class="photo" role="img" aria-label="Row of vertical CNC machining centres in a factory hall" style="left:127px;top:1892px;width:434px;height:412px;background:linear-gradient(180deg,#5d6670,#2f4e8a 50%,#8a8676)"></div>
<div class="svc" style="left:626px;top:1908px">
  <h3>CNC Machining</h3>
  <p>With our combination of high quality Torvane Machining Centres we are able to provide innovative solutions to your precision <span class="accent">CNC machining requirements.</span></p>
  <ul>
    <li><svg width="14" height="12" viewBox="0 0 14 12" fill="none" stroke="#111" stroke-width="1.5"><path d="M1 1l5 5-5 5M7 1l5 5-5 5"/></svg>Varying from general 2-D projects to more complex&nbsp; 3-D machining of prototypes and assemblies we are able to satisfy most medium size engineering requirements.</li>
    <li><svg width="14" height="12" viewBox="0 0 14 12" fill="none" stroke="#111" stroke-width="1.5"><path d="M1 1l5 5-5 5M7 1l5 5-5 5"/></svg>We host 3 different TORVANE Machines all with different advantages which helps us achieve a fast high quality product at a competitive price.</li>
  </ul>
</div>
<span class="btn" style="left:626px;top:2241px;width:118px;height:38px">Read More</span>

<div class="card" style="left:112px;top:2342px;width:978px;height:434px"></div>
<div class="svc" style="left:130px;top:2383px">
  <h3>EDM Wire Cutting</h3>
  <p>We operate Swiss manufactured Velmont EDM Machines which are regarded as the Aurex of wire cut machines.</p>
  <ul style="margin-top:12px">
    <li><svg width="14" height="12" viewBox="0 0 14 12" fill="none" stroke="#111" stroke-width="1.5"><path d="M1 1l5 5-5 5M7 1l5 5-5 5"/></svg>There is no limit to the hardness of material: as long as it is conductive we can cut it.</li>
    <li><svg width="14" height="12" viewBox="0 0 14 12" fill="none" stroke="#111" stroke-width="1.5"><path d="M1 1l5 5-5 5M7 1l5 5-5 5"/></svg>Wire cut machines are extremely accurate and leave and incredibly smooth surface which is not possible with other cutting methods.</li>
  </ul>
  <div class="key">Some of the key features:</div>
  <div class="specs"><span>5 - 10 micron accuracy</span><span>400mm height</span><span>30° taper cutting.</span><span>550mm X 350mm X 400mm</span></div>
</div>
<span class="btn" style="left:137px;top:2711px;width:120px;height:38px">Read More</span>
<div class="photo" role="img" aria-label="EDM wire cutting head working over a metal plate" style="left:643px;top:2354px;width:432px;height:412px;background:linear-gradient(160deg,#1d2d44,#6f86a8 50%,#2a3f5f)"></div>

<div class="card" style="left:112px;top:2792px;width:978px;height:436px"></div>
<div class="photo" role="img" aria-label="Metal 3D printer building a part layer by layer" style="left:129px;top:2805px;width:433px;height:412px;background:linear-gradient(160deg,#2a3342,#9aa6b6 55%,#3a4556)"></div>
<div class="svc" style="left:622px;top:2830px">
  <h3>3D Metal Printing</h3>
  <p style="line-height:21px">Sed ut perspiciatis unde omnis iste natus error sit voluptatem accusantium doloremque laudantium, totam rem aperiam</p>
  <ul>
    <li><svg width="14" height="12" viewBox="0 0 14 12" fill="none" stroke="#111" stroke-width="1.5"><path d="M1 1l5 5-5 5M7 1l5 5-5 5"/></svg>Nemo enim ipsam voluptatem quia voluptas sit aspernatur aut odit aut fugit, sed quia consequuntur magni sequi nesciunt.</li>
    <li><svg width="14" height="12" viewBox="0 0 14 12" fill="none" stroke="#111" stroke-width="1.5"><path d="M1 1l5 5-5 5M7 1l5 5-5 5"/></svg>Neque porro quisquam est, qui dolorem ipsum quia dolor sit amet, consectetu</li>
  </ul>
  <div class="key">Some of the key features:</div>
  <div class="specs" style="grid-template-columns:230px 200px"><span>Ut enim ad minima veniam</span><span>corporis suscipit</span><span>Quis nostrum exercitau</span><span>laboriosam nisi ut</span></div>
</div>
<span class="btn" style="left:626px;top:3162px;width:118px;height:38px">Read More</span>

<!-- TESTIMONIALS -->
<section class="abs testi">
  <h2>What Our Client Say?</h2>
  <div class="quote" style="left:114px;top:170px">
    <div class="avatar" role="img" aria-label="Client portrait"></div>
    <span class="who">Dane Corwell</span>
    <span class="rate"><svg width="90" height="14" viewBox="0 0 90 14"><circle cx="6" cy="7" r="6" fill="#fff"/><g fill="#f5b800"><path id="st" d="M22 1l1.8 4 4.2.4-3.2 2.8 1 4.2-3.8-2.2-3.8 2.2 1-4.2-3.2-2.8 4.2-.4z"/><use href="#st" x="14"/><use href="#st" x="28"/><use href="#st" x="42"/><use href="#st" x="56"/></g></svg></span>
    <p>Sed ut perspiciatis unde omnis iste natus error sit voluptatem accusantium doloremque laudantium, totam rem aperiam, eaque ipsa quae ab illo inventore veritatis et quasi architecto beatae vitae dicta sunt explicabo.</p>
  </div>
  <div class="abs" style="left:596px;top:180px;width:1px;height:200px;background:#5a6e80"></div>
  <div class="quote" style="left:646px;top:170px">
    <div class="avatar" role="img" aria-label="Client portrait" style="background:linear-gradient(#9cc4e0,#2f7fb8)"></div>
    <span class="who">Mira Halden</span>
    <span class="rate"><svg width="90" height="14" viewBox="0 0 90 14"><circle cx="6" cy="7" r="6" fill="#fff"/><g fill="#f5b800"><use href="#st"/><use href="#st" x="14"/><use href="#st" x="28"/><use href="#st" x="42"/><use href="#st" x="56"/></g></svg></span>
    <p>Nemo enim ipsam voluptatem quia voluptas sit aspernatur aut odit aut fugit, sed quia consequuntur magni dolores eos qui ratione voluptatem sequi nesciunt.</p>
  </div>
  <svg class="abs" style="left:31px;top:261px" width="22" height="22" viewBox="0 0 22 22"><circle cx="11" cy="11" r="11" fill="#fff"/><path d="M13 6l-5 5 5 5" fill="none" stroke="#111" stroke-width="2"/></svg>
  <svg class="abs" style="left:1149px;top:267px" width="22" height="22" viewBox="0 0 22 22"><circle cx="11" cy="11" r="11" fill="#fff"/><path d="M9 6l5 5-5 5" fill="none" stroke="#111" stroke-width="2"/></svg>
</section>

<!-- PROJECTS -->
<h2 class="sec-title" style="top:3828px">Recent <span class="accent">Projects</span></h2>
<div class="photo" role="img" aria-label="CNC machine spindle detail" style="left:0;top:3972px;width:383px;height:322px;background:linear-gradient(160deg,#2b3646,#8e9bad 55%,#3d4858)"></div>
<div class="abs proj-card">
  <h3>3D Metal Prining</h3>
  <p>Lorem ipsum dolor sit amet, consectetur adipiscing elit, sed do eiusmod tempor incididunt ut labore et dolore magna aliqua. Ut enim ad minim veniam, quis nostrud exercitation ullamco laboris nisi ut aliquip ex ea commodo consequat.</p>
  <a href="#">Read More....</a>
</div>
<div class="photo" role="img" aria-label="Machining tool cutting metal with chips" style="left:812px;top:3972px;width:388px;height:332px;background:linear-gradient(160deg,#0f1a2c,#3a5680 55%,#111a28)"></div>
<svg class="abs" style="left:31px;top:4146px" width="22" height="22" viewBox="0 0 22 22"><circle cx="11" cy="11" r="11" fill="#fff"/><path d="M13 6l-5 5 5 5" fill="none" stroke="#111" stroke-width="2"/></svg>
<svg class="abs" style="left:1149px;top:4146px" width="22" height="22" viewBox="0 0 22 22"><circle cx="11" cy="11" r="11" fill="#fff"/><path d="M9 6l5 5-5 5" fill="none" stroke="#111" stroke-width="2"/></svg>

<!-- FOOTER -->
<footer class="abs footer">
  <div class="logo" style="left:112px;top:78px">
    <span class="name" style="font-size:54px;line-height:1">KORVAL</span>
    <span class="tag" style="font-size:11px">PRECISION MACHINISTS</span>
  </div>
  <div class="abs" style="left:456px;top:76px;color:#fff;font:500 19px/28px Roboto,sans-serif">Join Our<br>Newsletter</div>
  <div class="abs" style="left:597px;top:55px;width:353px;height:58px;background:#fff;color:#333;font-size:13px;padding:22px 22px">Enter Email address</div>
  <span class="btn" style="left:950px;top:55px;width:138px;height:58px">Subscribe</span>
  <div class="abs" style="left:112px;top:178px;width:976px;height:1px;background:#4a5b6a"></div>

  <div class="col" style="left:115px"><h4>Quick Links</h4><a>Home</a><a>About Us</a><a>Services</a><a>Projects</a><a>Testimonials</a><a>Contact Us</a></div>
  <div class="vline" style="left:310px"></div>
  <div class="col" style="left:355px"><h4>Other Links</h4><a>Privacy Police</a><a>Terms &amp; Conditions</a><a>Disclaimer</a></div>
  <div class="vline" style="left:555px"></div>
  <div class="col" style="left:600px;top:185px"><h4 style="margin-bottom:10px">Contact Info</h4>
    <div class="row"><svg width="20" height="20" viewBox="0 0 20 20"><rect width="20" height="20" rx="3" fill="#fff"/><path d="M10 4a4 4 0 0 0-4 4c0 3 4 8 4 8s4-5 4-8a4 4 0 0 0-4-4z" fill="#0c1d2c"/></svg>Lorem Ipsum ,Usa -437916</div>
    <div class="row"><svg width="20" height="20" viewBox="0 0 20 20"><rect width="20" height="20" rx="3" fill="#fff"/><path d="M6 4l3 3-1.5 2a8 8 0 0 0 3.5 3.5L13 11l3 3-2 2C9 16 4 11 4 6z" fill="#0c1d2c"/></svg>+1 888 888 88888</div>
    <div class="row"><svg width="20" height="20" viewBox="0 0 20 20"><rect width="20" height="20" rx="3" fill="#fff"/><rect x="4" y="6" width="12" height="9" fill="none" stroke="#0c1d2c" stroke-width="1.5"/><path d="M4 6l6 5 6-5" fill="none" stroke="#0c1d2c" stroke-width="1.5"/></svg>info@korvalprecisionmachinists.in</div>
  </div>
  <div class="vline" style="left:913px"></div>
  <div class="col" style="left:985px;top:185px"><h4 style="margin-bottom:12px">Follow Us</h4>
    <div class="soc"><i></i>Friendloop</div>
    <div class="soc"><i></i>Snapgrid</div>
    <div class="soc"><i></i>Chirper</div>
    <div class="soc"><i></i>Worknet</div>
  </div>
  <div class="copy">© 2024 Korval precision machinists. All rights reserved.</div>
</footer>

</body>
</html>
```